Hollyfern Yuletide Firs needs words putting into pictures!

Hollyfern Yuletide Firs sells real Christmas Trees directly to consumers and retailers. A "growing" part of our business is fulfilling online orders e.g. a garden centre sells a tree online, and we do everything else from selecting the tree to delivery. We are now looking to market this service as best in class due to the selection process we have, and a link up we have made with a courier company.

We want to summarise the process into a simple one page graphic that illustrates the process from start to finish in simple language, short sentences, with images and pictures.

Given how difficult it is to get good images of Christmas trees, we thought simple outline pictures could work - almost like sketches. We are open to all ideas.

We can provide any of the images in the attached brochure, and many more depending what you may require.

We like clean cut, simple designs that are clear and innovative.

Contact Information for Business Card

Martin Crane, Director, Hollyfern Yuletide Firs, martin@hollyfernyuletidefirs.com, Brookside Meadow, Fenwick Road, Marbury Heath, LT4 9QD

Font styles to use
Sans Serif

Colors
00a990

Requirements
Must have
• Condense the info down into a manageable graphic that shows our customers clearly what service we are able to provide
Nice to have
• Simple, elegant design to compliment brand feel
Should not have
• Not be too complicated

```html
<!DOCTYPE html>
<html lang="en">
<head>
<meta charset="utf-8">
<title>How Your Tree Is Selected – Hollyfern Yuletide Firs</title>
<link rel="stylesheet" href="https://fonts.googleapis.com/css2?family=Fredoka:wght@500&family=Questrial&display=swap">
<style>
  :root {
    --forest-dark: #2f6a4a;
    --forest-mid: #5f9a72;
    --forest-light: #a9cfae;
    --title-ink: #2d2a55;
    --accent-yellow: #ffe600;
    --heading-green: #8cbf26;
    --band-grey: #ececec;
    --band-light: #f4f4f4;
    --body-ink: #262626;
    --rule-ink: #2b2b2b;
    --brand-green: #1c8a3a;
    --illus-tan: #ecd3a6;
    --illus-green: #cfe3d3;
    --illus-grey: #dcdcdc;
    --illus-red: #f4d2cc;
    --paper: #ffffff;
  }
  * { box-sizing: border-box; margin: 0; padding: 0; }
  html, body { width: 1200px; height: 2353px; overflow: hidden; background: var(--paper); }
  .infographic { position: relative; width: 1200px; height: 2353px; font-family: "Questrial", sans-serif; color: var(--body-ink); }

  .hero { position: absolute; left: 0; top: 0; width: 1200px; height: 357px; }
  .hero-forest { position: absolute; inset: 0; background: linear-gradient(180deg, #e4f0e6 0%, var(--forest-light) 35%, var(--forest-mid) 70%, var(--forest-dark) 100%); }
  .hero-title { position: absolute; left: 0; right: 0; top: 42px; text-align: center; font-family: "Fredoka", sans-serif; font-weight: 500; font-size: 84px; line-height: 104px; color: var(--title-ink); -webkit-text-stroke: 2px var(--paper); paint-order: stroke fill; }
  .hero-rule { position: absolute; left: 0; top: 357px; width: 1200px; height: 11px; background: var(--accent-yellow); }

  .step { position: absolute; left: 0; width: 1200px; }
  .step--grey { background: var(--band-grey); }
  .step--light { background: var(--band-light); }
  .step-title { position: absolute; font-weight: 400; font-size: 57px; line-height: 68px; color: var(--heading-green); white-space: nowrap; }
  .step-rule { position: absolute; height: 2px; background: var(--rule-ink); }
  .step-text { position: absolute; width: 555px; font-size: 21.5px; line-height: 30.5px; }
  .step-text--right { text-align: right; }
  .step-illustration { position: absolute; border-radius: 50%; }

  .footer { position: absolute; left: 0; top: 2120px; width: 1200px; height: 233px; background: var(--paper); }
  .brand { position: absolute; left: 110px; top: 70px; display: flex; align-items: center; gap: 22px; }
  .brand-mark { width: 46px; height: 46px; background: var(--brand-green); }
  .brand-name { font-size: 34px; line-height: 38px; color: var(--brand-green); }
  .footer-divider { position: absolute; left: 558px; top: 30px; width: 2px; height: 166px; background: var(--brand-green); }
  .contact { position: absolute; left: 650px; top: 74px; list-style: none; font-size: 23px; line-height: 34px; color: var(--brand-green); }
</style>
</head>
<body>
<main class="infographic">
  <header class="hero">
    <div class="hero-forest" role="img" aria-label="Illustrated pine forest in layered shades of green"></div>
    <h1 class="hero-title">How Your Tree<br>Is Selected</h1>
  </header>
  <div class="hero-rule"></div>

  <section class="step step--grey" style="top:368px;height:350px;">
    <h2 class="step-title" style="left:34px;top:34px;">Careful selection</h2>
    <div class="step-rule" style="left:0;top:102px;width:495px;"></div>
    <p class="step-text" style="left:38px;top:133px;">Every order is matched to a tree by hand. Our growers walk the fields and choose each fir for its shape, height, colour and full, even branches, so you receive a tree that looks just as good as the one you picked online.</p>
    <div class="step-illustration" style="left:700px;top:20px;width:470px;height:310px;border-radius:12px;background:radial-gradient(ellipse at 50% 45%, var(--illus-green) 0%, var(--illus-grey) 100%);" role="img" aria-label="Claw picking one green tree from a row of grey trees"></div>
  </section>

  <section class="step step--light" style="top:718px;height:350px;">
    <div class="step-illustration" style="left:55px;top:42px;width:266px;height:290px;background:radial-gradient(circle at 50% 40%, var(--illus-green) 0%, var(--illus-tan) 100%);" role="img" aria-label="Open hand holding a small glowing tree"></div>
    <h2 class="step-title" style="right:44px;top:34px;">Maximum freshness</h2>
    <div class="step-rule" style="left:611px;top:104px;width:589px;"></div>
    <p class="step-text step-text--right" style="right:33px;top:136px;">Your tree is cut only once your order is confirmed, never weeks in advance. It leaves our farm within hours of felling, so the needles stay soft, green and fragrant, and the tree lasts well past the festive season.</p>
  </section>

  <section class="step step--grey" style="top:1068px;height:350px;">
    <h2 class="step-title" style="left:34px;top:26px;">Efficient transport</h2>
    <div class="step-rule" style="left:0;top:99px;width:522px;"></div>
    <p class="step-text" style="left:38px;top:150px;">Through our partner courier, each tree travels straight from the farm to the door with no warehouse stops. Most orders arrive within two working days, and you can track the delivery every step of the way.</p>
    <div class="step-illustration" style="left:757px;top:18px;width:340px;height:314px;border-radius:12px;background:radial-gradient(ellipse at 50% 40%, var(--illus-tan) 0%, var(--illus-red) 100%);" role="img" aria-label="Delivery truck carrying a boxed tree"></div>
  </section>

  <section class="step step--light" style="top:1418px;height:352px;">
    <div class="step-illustration" style="left:63px;top:50px;width:305px;height:286px;background:radial-gradient(ellipse at 50% 50%, var(--illus-green) 0%, var(--illus-tan) 100%);" role="img" aria-label="Two hands protectively cupping a tree"></div>
    <h2 class="step-title" style="right:44px;top:28px;">Damage prevention</h2>
    <div class="step-rule" style="left:608px;top:102px;width:592px;"></div>
    <p class="step-text step-text--right" style="right:45px;top:144px;">Each tree is gently netted and packed in a sturdy, made-to-measure box. The branches stay protected from knocks and bending in transit, so your tree opens out in full shape the moment it is unwrapped.</p>
  </section>

  <section class="step step--grey" style="top:1770px;height:350px;">
    <h2 class="step-title" style="left:34px;top:24px;line-height:68px;">Multiple stages of<br>quality control</h2>
    <div class="step-rule" style="left:0;top:171px;width:602px;"></div>
    <p class="step-text" style="left:38px;top:196px;">Every tree is checked when chosen, checked again when packed and checked once more before it leaves the farm. Only trees that pass all three stages are sent out to our customers.</p>
    <div class="step-illustration" style="left:815px;top:40px;width:305px;height:290px;border-radius:12px;background:radial-gradient(ellipse at 60% 45%, var(--paper) 0%, var(--illus-grey) 100%);" role="img" aria-label="Hand ticking a five-star rating on a quality checklist"></div>
  </section>

  <footer class="footer">
    <div class="brand">
      <span class="brand-mark"></span>
      <span class="brand-name">Hollyfern<br>Yuletide Firs</span>
    </div>
    <div class="footer-divider"></div>
    <ul class="contact">
      <li>+44 (0)1632 960418</li>
      <li>sales@hollyfernyuletidefirs.com</li>
      <li>www.hollyfernyuletidefirs.com</li>
    </ul>
  </footer>
</main>
</body>
</html>
```